Flowy subpage design wanted for a modern tax/accounting firm in Switzerland

--- Introduction ---
We are a tax and accounting firm in Switzerland. We provide services for expats living in Switzerland, our service is quite exclusive and modern (digital).

We just relaunched our website www.fiscaverde.ch and are happy with the design, so the desired subpage (more details below) should of course fit in.

--- Main brief ---
Please see Word File attached. The page has to include the whole text (11 chapters). A very intuitive, flowy design on only one subpage (not one page per chapter) is a MUST. Also, it is key that the design is supporting the content of the individual chapters, so it would be advantageous if you'd have a good unterstanding of the text attached.

--- Further information ---
A similar example would be this one: https://www2.brennmark.com/ch/en/pages/tax/articles/living-working-switzerland.html

This one is similar in what concerns the content, but NOT what we are looking for designwise. It is very simple and looks "thrown together", just not aesthetically pleasing in our opinion.

--- Final thoughts ---
- If you blow our minds with your design, we will certainly have future work for you.
- Our clients are between 20-50 years old, well educated, high income / high wealth, English speaking and living in Switzerland.
- CI/CD information:
Fonts
Montserrat regular / medium italic / bold
Colors
White #ffffffff
Darkblue #0a2b46
Darkblue 25% #b5bfc8
Darkblue 50% #8595a4
Greenblue #0d4261

We are looking forward to your designs!
Updates

Thank you very much for the submitted designs and your efforts. Unfortunately, none of the designs meet our expectations so far. Please note the following: - Designs that do not take CI into account will not be looked at more closely. - We have received many simple designs with very simple structure and accordion elements. But more important than the simple structure is an eye-catching design! Make it flowy and beautiful - We don't want pictures of Swiss vehicles, passes or other pictures that don't actively support the text. If you can make an illustration that really fits the context, fine, otherwise better leave it without. Thank you

Target Market(s)

Expats living in Switzerland. High income earners / high net worth individuals

Industry/Entity Type

tax/accounting

Number of Pages Required

1 page

Font styles to use
Other font styles liked:
• Montserrat

Colors
0054AA
0677BA
7BADD7
CADEEF
E8F1F8

Requirements
Must have
• based on general website design
Nice to have
• intuitive, flowy, attractive representation of much text
Should not have
• basic copy/paste of the text in sections :)

```html
<!DOCTYPE html>
<html lang="en">
<head>
<meta charset="utf-8">
<title>Switzerland – Swiss tax guide | Fiscaverde Advisory</title>
<link href="https://fonts.googleapis.com/css2?family=Montserrat:ital,wght@0,400;0,500;0,600;0,700;1,500&display=swap" rel="stylesheet">
<style>
:root{
  --white:#ffffff;
  --darkblue:#0a2b46;
  --darkblue-25:#b5bfc8;
  --darkblue-50:#8595a4;
  --greenblue:#0d4261;
  --blue:#0677BA;
  --blue-strong:#0054AA;
  --blue-light:#CADEEF;
  --blue-pale:#E8F1F8;
  --text:#2a2f36;
}
*{box-sizing:border-box;margin:0;padding:0}
html,body{width:1200px;height:3038px;overflow:hidden}
body{font-family:'Montserrat',sans-serif;background:var(--white);color:var(--text);position:relative}

/* Header */
.site-header{position:absolute;top:0;left:0;width:1200px;height:57px;background:#f4f5f6}
.brand{position:absolute;left:100px;top:8px;display:flex;align-items:center;gap:8px;color:var(--darkblue);font-weight:700;font-size:15px;line-height:17px;letter-spacing:.5px}
.brand-mark{width:40px;height:40px;border-radius:50%;background:var(--darkblue)}
.main-nav{position:absolute;left:579px;top:0;height:57px;display:flex;gap:20px;align-items:center;font-size:10px;color:#4a5663}
.main-nav a{color:inherit;text-decoration:none;height:57px;display:flex;align-items:center}
.main-nav a.active{color:var(--darkblue);font-weight:600;border-bottom:2px solid var(--darkblue);padding:0 10px}
.btn-calc{position:absolute;left:1006px;top:14px;width:90px;height:28px;background:var(--greenblue);color:var(--white);font-size:10px;display:flex;align-items:center;justify-content:center;gap:8px}
.btn-calc svg{width:10px;height:12px}

/* Hero */
.hero{position:absolute;top:57px;left:0;width:1200px;height:290px}
.hero-photo{position:absolute;inset:0;background:linear-gradient(180deg,#6fa3d6 0%,#b9d3ea 28%,#7d8b7a 52%,#4f6b3f 75%,#3f5a34 100%)}
.hero h1{position:absolute;top:95px;width:100%;text-align:center;color:var(--white);font-weight:600;font-size:38px;letter-spacing:.5px}
.hero-edge{position:absolute;left:0;bottom:0;width:1200px;height:120px}
.search{position:absolute;left:346px;top:225px;width:506px;height:50px;background:var(--white);box-shadow:0 4px 14px rgba(10,43,70,.18);display:flex;align-items:center}
.search span{margin-left:40px;font-size:9px;color:var(--darkblue-25)}
.search-btn{position:absolute;right:8px;top:6px;width:85px;height:38px;background:var(--greenblue);display:flex;align-items:center;justify-content:center}

/* Sidebar */
.toc{position:absolute;left:88px;top:398px;width:244px;font-size:9.6px;font-weight:600;color:var(--darkblue);line-height:12px}
.toc li{list-style:none;position:relative}
.toc .l1{padding:4px 20px 4px 0}
.toc .group{border-left:1.5px solid var(--darkblue)}
.toc .l2{padding:4px 20px 4px 24px}
.toc .sub3{border-left:1.5px solid var(--darkblue);margin-left:24px}
.toc .sub3 .l3{padding:4px 20px 4px 24px}
.chev{position:absolute;right:2px;top:6px;width:8px;height:8px}

/* Article */
.article{position:absolute;left:397px;top:402px;width:680px;font-size:10.5px;line-height:18.7px}
.article h2{font-size:15.5px;font-weight:600;color:var(--darkblue);margin-bottom:20px}
.article h3{font-size:14.5px;font-weight:600;color:var(--darkblue);margin:22px 0 20px}
.article h4{font-size:13px;font-weight:500;color:var(--blue);margin:22px 0 20px}
.article p{margin:0}
.article ul.dots{margin-left:42px;list-style:none}
.article ul.dots li::before{content:"• "}
.note{color:#1d5a8c}
.school{list-style:none;margin:20px 0 22px 32px}
.school li{display:flex;align-items:flex-start;gap:26px;min-height:40px}
.school svg{flex:0 0 24px;height:24px;margin-top:-3px}
</style>
</head>
<body>

<header class="site-header">
  <div class="brand"><span class="brand-mark"></span><span>FISCAVERDE<br>ADVISORY</span></div>
  <nav class="main-nav">
    <a href="#">Home</a><a href="#">Tax returns</a><a href="#">More services ▾</a><a href="#" class="active">Swiss tax guide</a><a href="#">About us</a>
  </nav>
  <a class="btn-calc"><svg viewBox="0 0 10 12"><rect x="0.5" y="0.5" width="9" height="11" fill="none" stroke="#fff"/><rect x="2" y="2" width="6" height="2" fill="#fff"/></svg>Calculate</a>
</header>

<section class="hero">
  <div class="hero-photo" role="img" aria-label="Photo of a green alpine valley with forested mountain slopes under a blue sky"></div>
  <h1>Switzerland</h1>
  <svg class="hero-edge" viewBox="0 0 1200 120" preserveAspectRatio="none">
    <path d="M0 120 L0 118 C300 100 600 85 852 62 L1200 30 L1200 120 Z" fill="#fff"/>
    <path d="M852 60 L1200 8 L1200 70 C1080 66 960 66 852 62 Z" fill="#0a2b46"/>
  </svg>
  <div class="search"><span>Search</span>
    <div class="search-btn"><svg width="16" height="16" viewBox="0 0 16 16"><circle cx="7" cy="7" r="5.5" fill="none" stroke="#fff" stroke-width="1.5"/><line x1="11" y1="11" x2="14.5" y2="14.5" stroke="#fff" stroke-width="1.5"/></svg></div>
  </div>
</section>

<nav class="toc">
  <ul>
    <li class="l1">Life in Switzerland<svg class="chev" viewBox="0 0 8 8"><path d="M1 2.5 4 5.5 7 2.5" fill="none" stroke="#0a2b46" stroke-width="1.3"/></svg></li>
    <li class="group"><ul>
      <li class="l2">General<svg class="chev" viewBox="0 0 8 8"><path d="M1 2.5 4 5.5 7 2.5" fill="none" stroke="#0a2b46" stroke-width="1.3"/></svg></li>
      <li class="sub3"><ul>
        <li class="l3">4 official languages</li>
        <li class="l3">Currency and banking</li>
        <li class="l3">Public holidays</li>
        <li class="l3">Usual business and store opening hours</li>
        <li class="l3">Electricity and water</li>
        <li class="l3">Telephone and television</li>
      </ul></li>
      <li class="l2">Living in Switzerland<svg class="chev" viewBox="0 0 8 8"><path d="M5.5 1 2.5 4 5.5 7" fill="none" stroke="#0a2b46" stroke-width="1.3"/></svg></li>
      <li class="l2">The education system in Switzerland</li>
      <li class="l2">The healthcare system in Switzerland</li>
      <li class="l2">Driving in Switzerland<svg class="chev" viewBox="0 0 8 8"><path d="M5.5 1 2.5 4 5.5 7" fill="none" stroke="#0a2b46" stroke-width="1.3"/></svg></li>
      <li class="l2">Public transport in Switzerland<svg class="chev" viewBox="0 0 8 8"><path d="M5.5 1 2.5 4 5.5 7" fill="none" stroke="#0a2b46" stroke-width="1.3"/></svg></li>
    </ul></li>
    <li class="l1">Switzerland - a brief overview of the Alpine country<svg class="chev" viewBox="0 0 8 8"><path d="M1 2.5 4 5.5 7 2.5" fill="none" stroke="#0a2b46" stroke-width="1.3"/></svg></li>
    <li class="group"><ul>
      <li class="l2">A strong federation</li>
      <li class="l2">A diverse population structure</li>
      <li class="l2">Excellent economy</li>
      <li class="l2">High standard of living</li>
      <li class="l2">Exemplary pension system</li>
    </ul></li>
    <li class="l1">Immigrating to Switzerland - These options are available<svg class="chev" viewBox="0 0 8 8"><path d="M1 2.5 4 5.5 7 2.5" fill="none" stroke="#0a2b46" stroke-width="1.3"/></svg></li>
    <li class="group"><ul>
      <li class="l2">Immigrants with EU/EFTA citizenship</li>
      <li class="l2">Immigrants from a third country</li>
      <li class="l2">Overview of the different work/establishment passes<svg class="chev" viewBox="0 0 8 8"><path d="M5.5 1 2.5 4 5.5 7" fill="none" stroke="#0a2b46" stroke-width="1.3"/></svg></li>
    </ul></li>
    <li class="l1">Labor Law in Switzerland - An Overview<svg class="chev" viewBox="0 0 8 8"><path d="M1 2.5 4 5.5 7 2.5" fill="none" stroke="#0a2b46" stroke-width="1.3"/></svg></li>
    <li class="group"><ul>
      <li class="l2">The employment contract</li>
      <li class="l2">Probationary period</li>
      <li class="l2">Termination of the employment relationship</li>
      <li class="l2">When may the employer not terminate?</li>
    </ul></li>
    <li class="l1">Double taxation agreements between Switzerland and other countries<svg class="chev" viewBox="0 0 8 8"><path d="M1 2.5 4 5.5 7 2.5" fill="none" stroke="#0a2b46" stroke-width="1.3"/></svg></li>
    <li class="group"><ul>
      <li class="l2">Taxation of income and assets</li>
      <li class="l2">Double taxation in the case of gifts or inheritances</li>
      <li class="l2">Countries with which Switzerland has a double taxation agreement</li>
    </ul></li>
    <li class="l1">Indirect taxes in Switzerland<svg class="chev" viewBox="0 0 8 8"><path d="M1 2.5 4 5.5 7 2.5" fill="none" stroke="#0a2b46" stroke-width="1.3"/></svg></li>
    <li class="group"><ul>
      <li class="l2">Value added tax<svg class="chev" viewBox="0 0 8 8"><path d="M5.5 1 2.5 4 5.5 7" fill="none" stroke="#0a2b46" stroke-width="1.3"/></svg></li>
      <li class="l2">Indirect taxes incurred when moving<svg class="chev" viewBox="0 0 8 8"><path d="M5.5 1 2.5 4 5.5 7" fill="none" stroke="#0a2b46" stroke-width="1.3"/></svg></li>
    </ul></li>
    <li class="l1">Other federal taxes in Switzerland<svg class="chev" viewBox="0 0 8 8"><path d="M1 2.5 4 5.5 7 2.5" fill="none" stroke="#0a2b46" stroke-width="1.3"/></svg></li>
    <li class="group"><ul>
      <li class="l2">Stamp duty</li>
      <li class="l2">Withholding tax</li>
      <li class="l2">EU Savings Directive</li>
    </ul></li>
    <li class="l1">Rent and buy in Switzerland<svg class="chev" viewBox="0 0 8 8"><path d="M1 2.5 4 5.5 7 2.5" fill="none" stroke="#0a2b46" stroke-width="1.3"/></svg></li>
    <li class="group"><ul>
      <li class="l2">Average prices</li>
      <li class="l2">Renting is popular</li>
      <li class="l2">Rent property - what you need to consider<svg class="chev" viewBox="0 0 8 8"><path d="M5.5 1 2.5 4 5.5 7" fill="none" stroke="#0a2b46" stroke-width="1.3"/></svg></li>
      <li class="l2">Buying residential property - Paying attention to taxes<svg class="chev" viewBox="0 0 8 8"><path d="M5.5 1 2.5 4 5.5 7" fill="none" stroke="#0a2b46" stroke-width="1.3"/></svg></li>
    </ul></li>
    <li class="l1">Childcare in Switzerland<svg class="chev" viewBox="0 0 8 8"><path d="M1 2.5 4 5.5 7 2.5" fill="none" stroke="#0a2b46" stroke-width="1.3"/></svg></li>
    <li class="group"><ul>
      <li class="l2">Different types of care<svg class="chev" viewBox="0 0 8 8"><path d="M5.5 1 2.5 4 5.5 7" fill="none" stroke="#0a2b46" stroke-width="1.3"/></svg></li>
      <li class="l2">Tax benefits for external childcare<svg class="chev" viewBox="0 0 8 8"><path d="M5.5 1 2.5 4 5.5 7" fill="none" stroke="#0a2b46" stroke-width="1.3"/></svg></li>
    </ul></li>
    <li class="l1">Public transportation<svg class="chev" viewBox="0 0 8 8"><path d="M1 2.5 4 5.5 7 2.5" fill="none" stroke="#0a2b46" stroke-width="1.3"/></svg></li>
    <li class="group"><ul>
      <li class="l2">The public transport network<svg class="chev" viewBox="0 0 8 8"><path d="M5.5 1 2.5 4 5.5 7" fill="none" stroke="#0a2b46" stroke-width="1.3"/></svg></li>
    </ul></li>
    <li class="l1">Recreation<svg class="chev" viewBox="0 0 8 8"><path d="M1 2.5 4 5.5 7 2.5" fill="none" stroke="#0a2b46" stroke-width="1.3"/></svg></li>
    <li class="group"><ul>
      <li class="l2">Sports clubs</li>
      <li class="l2">Volunteer</li>
      <li class="l2">Integration courses</li>
      <li class="l2">Mingle with the people</li>
    </ul></li>
  </ul>
</nav>

<main class="article">
  <h2>1. Life in Switzerland</h2>
  <p>To give you a small impression of what to expect when living in Switzerland, we have put together some topics for you to make your new start in Switzerland as pleasant as possible.</p>

  <h3>General</h3>
  <h4>4 official languages</h4>
  <p>Unlike many other countries in Europe, where there is usually only one official national language, Switzerland has four of them: German, French, Italian and Romansh.<br>
  The most widespread language is German, which is spoken mainly in central Switzerland and the cantons bordering Germany.<br>
  French dominates in the western part of Switzerland, and Italian in the southeastern part.<br>
  Rhaeto-Romanic is spoken by only a very small part of the total population in eastern Switzerland.<br>
  In each region, there are also different dialects in the various languages.<br>
  Official documents are generally issued in German, French and Italian.</p>

  <h4>Currency and banking</h4>
  <p class="note">The national currency in Switzerland is the Swiss franc (CHF). 1 Swiss franc (Franken) is equal to 100 centimes (Rappen).<br>
  The banknotes are available in the following amounts: 10, 20, 50, 100, 200, 1000.<br>
  For coins, there are the following denominations:</p>
  <ul class="dots note"><li>CHF 1, 2, 5</li><li>5, 10, 20, 50 centimes</li></ul>
  <p class="note">Current accounts can be opened at any major bank, Swiss Postal Savings, cantonal or private banks. The largest banks in Switzerland are: Alpen Credit, UBK and PostBanca.</p>

  <h4>Public holidays</h4>
  <p>Public holidays apply throughout Switzerland. In addition, there are cantonal holidays, which may vary from canton to canton.<br>The federal public holidays are:</p>
  <ul class="dots">
    <li>January 1: New Year's Day</li><li>Good Friday (variable date)</li><li>Easter Monday (variable date)</li>
    <li>Ascension Day (variable date, 38 days after Easter Monday)</li><li>August 1: Swiss National Day</li>
    <li>December 25: Christmas Day</li><li>December 26: Boxing Day</li>
  </ul>

  <h4>Usual business and store opening hours</h4>
  <p>Government offices and banks are typically open from 8 a.m. to 5 p.m. on weekdays (Monday through Friday), although there may be differences depending on the office.<br>
  Stores are usually open from 9 a.m. to 6:30 p.m. on weekdays, and from 9 a.m. to 5 p.m. on Saturdays. In cities, stores are often open even later, until 9 pm.<br>
  Stores, banks and government offices are generally closed on Sundays. Exceptions are stores in train stations, airports or tourist places.</p>

  <h4>Electricity and water</h4>
  <p>The provision and maintenance of the public electricity and water network is the responsibility of the cantons. As a rule, anyone moving into a house or apartment must register their electricity connection with a supplier of their choice. The monthly, quarterly or semi-annual contributions are then paid by means of a progress bill. The energy supplier, as well as the water company, usually prepare a statement at the end of the year, and refund overpaid contributions, or demand an</p>

  <h4>Telephone and television</h4>
  <p>The Swiss telephone network is operated by Helvanet. Anyone who wants to have a telephone or Internet connection must contact Helvanet so that it provides a connection (if not already available). Any service can then be selected as the Internet provider.<br>
  Every household must pay a broadcasting fee - even if there is no TV or radio. The fees are collected by the MEDIAFEE company.</p>

  <h3>Living in Switzerland</h3>
  <p>The Swiss housing and real estate market varies greatly from region to region in terms of purchase and rental prices. In highly sought-after areas or larger cities, prices are relatively high, while living in rural areas is less expensive.</p>
  <h4>Rent</h4>
  <p>Vacancies are the exception rather than the rule in highly sought-after regions. Often, rental properties are not even published on the Internet, so it is more difficult to find a suitable apartment without a real estate agent. A real estate agent has access to properties before they are published by advertisement. This increases the chances of finding a property for rent. However, the landlord always has the final say. The landlord is not obliged to accept the first applicant.</p>
  <h4>Buy</h4>
  <p>Under certain conditions, it is also possible for non-Swiss nationals to purchase residential property in Switzerland.<br>
  A down payment of 20% of the purchase price must be made from equity, as a maximum mortgage of 80% of the purchase price can be taken out.<br>
  The purchase of a property changes the tax situation of the buyer, as the residential property is henceforth included in the assets and is therefore subject to wealth tax (which varies from canton to canton). It is advisable to consult with a tax expert</p>

  <h3>The education system in Switzerland</h3>
  <p>In Switzerland, there are both public and private schools. The public schools are financed by the cantons and attendance at such a school is free of charge.<br>
  Compulsory kindergarten or schooling begins at the age of 4. A minimum of 11 years of schooling is compulsory.<br>
  Public educational institutions are classified as follows:</p>
  <ul class="school">
    <li><svg viewBox="0 0 24 24"><circle cx="12" cy="12" r="12" fill="#0677BA"/><circle cx="12" cy="12" r="5" fill="none" stroke="#fff" stroke-width="1.5"/></svg><span>Kindergarten: age 4-6 years; compulsory in most cantons</span></li>
    <li><svg viewBox="0 0 24 24"><circle cx="12" cy="12" r="12" fill="#0677BA"/><rect x="7" y="9" width="10" height="7" fill="none" stroke="#fff" stroke-width="1.5"/></svg><span>Elementary school: ages 6-12, grades 1-6, mandatory.</span></li>
    <li><svg viewBox="0 0 24 24"><circle cx="12" cy="12" r="12" fill="#0677BA"/><rect x="8" y="7" width="8" height="10" fill="none" stroke="#fff" stroke-width="1.5"/></svg><span>secondary school: age 12-15, compulsory, leads to completion of compulsory education plan</span></li>
    <li><svg viewBox="0 0 24 24"><circle cx="12" cy="12" r="12" fill="#0677BA"/><path d="M6 11 12 8 18 11 12 14Z" fill="#fff"/></svg><span>after secondary school: special schools for preparation for higher education (e.g. university), or training centers for trainees</span></li>
  </ul>
  <p>Anyone wishing to enroll their child in the Swiss public school system must contact the cantonal education authority and provide the following proof:</p>
  <ul class="dots" style="margin-left:40px"><li>Work/residence permit for Switzerland</li><li>Health and accident insurance for the child</li></ul>
  <p>If a foreign child is between the ages of 12 and 15, he or she must pass an entrance exam before enrolling in a public school, which tests, among other things, sufficient proficiency in the language of instruction.<br>
  Enrolling the child in a private school is also possible. However, depending on the school, waiting times for a free place can be several years.</p>

  <h3>The healthcare system in Switzerland</h3>
  <p>The healthcare system in Switzerland is one of the best in the world. Even in less densely populated regions, the density of hospitals and doctors' offices is high, so that medical care is always timely manner.<br>
  The federal government sets the financial framework within which health insurers may offer their premiums. The federal government must also give its prior consent to premium increases and can also reject them.<br>
  The cantons and municipalities are responsible for regulating hospitals. This means that it is determined at the cantonal level which hospital provides which services and how high the wages of doctors and nursing staff are.<br>
  Compulsory health insurance applies in Switzerland. This means that everyone who lives here must have health insurance.<br>
  The health insurance companies are private companies, but they are only allowed to operate within the legal framework set by the federal government.<br>
  The companies are obliged to include every citizen in the so-called basic insurance- without a prior health check<br>
  Insured persons can add additional services that go beyond basic medical care to their health insurance plan at an additional cost, if they wish.<br>
  Every citizen is free to choose an insurer. The amount of the insurance premiums that are paid monthly differ in part very much from insurer to insurer. Therefore, it is advisable to compare the benefits and premiums of the individual insurers beforehand.</p>

  <h3>Driving in Switzerland</h3>
  <h4>General information about driving in Switzerland</h4>
  <p>Right-hand traffic applies in Switzerland. Driving a vehicle is permitted for persons 18 years of age and older; trucks and other large vehicles may only be driven from 21 years of age. Fun fact: A small motorcycle or a tractor can already be driven from 14 years upwards.<br>
  In order to be able to drive on freeways, a vignette must be purchased every year. This can be obtained at customs or at gas stations. The price is currently CHF 40.<br>
  On highways, the maximum speed is 120km/h, unless otherwise indicated by a sign. A maximum speed of 50km/h applies in built-up areas.</p>
</main>

</body>
</html>
```